New Theme For Our Sales Sheets and Full Brochure

I need a new theme for a refrigerated cooler display. This them will get used for approx. 10 different items as well as a Full Brochure. If the feedback is great, we will change our website to follow the same theme.

I want to see how you can create a clean, simple sales sheet that will highlight features and help customers picture their products in our displays.

I have included in the file uploads a sales sheet from the past that we want to create something totally different

Target Market(s)

Supermarkets

Industry/Entity Type

Sales

Font styles to use
Serif

Requirements
Must have
• A very attractive theme that helps a viewer picture THEIR products in the coolers.
• Only want to show (2) units on the sales sheet... (1) Curved Header and (1) Flat.
Nice to have
• Highlight the feature of either a Curved or Flat Header that is back lit.

```html
<!DOCTYPE html>
<html lang="en">
<head>
<meta charset="utf-8">
<title>Grab N Go Refrigerated Displays – Sales Sheet</title>
<link href="https://fonts.googleapis.com/css2?family=Playfair+Display:wght@400;600;700&family=Source+Serif+4:wght@400;600&display=swap" rel="stylesheet">
<style>
  :root {
    --paper: #f7fafb;
    --ice: #e3eff3;
    --frost: #cfe3ea;
    --navy: #14304a;
    --teal: #1f6f80;
    --glow: #ffe6a6;
    --ink: #1c2630;
    --muted: #52606b;
    --line: #b9cfd7;
    --white: #ffffff;
  }
  * { margin: 0; padding: 0; box-sizing: border-box; }
  html, body { width: 927px; height: 1200px; overflow: hidden; }
  body { font-family: "Source Serif 4", Georgia, serif; color: var(--ink); background: var(--paper); }

  .sheet {
    width: 927px; height: 1200px; overflow: hidden;
    display: flex; flex-direction: column;
    background: linear-gradient(180deg, var(--white) 0%, var(--paper) 45%, var(--ice) 100%);
  }

  .brand-bar {
    height: 92px; flex: none;
    display: flex; align-items: center; justify-content: space-between;
    padding: 0 56px;
    border-bottom: 1px solid var(--line);
  }
  .brand-name {
    display: flex; align-items: center; gap: 12px;
    font-family: "Source Serif 4", Georgia, serif;
    font-size: 22px; font-weight: 600; letter-spacing: 2px;
    color: var(--navy);
  }
  .brand-mark { width: 14px; height: 14px; background: var(--teal); }
  .brand-web { font-size: 16px; color: var(--muted); }

  .headline { height: 170px; flex: none; padding: 34px 56px 0; }
  .headline h1 {
    font-family: "Playfair Display", Georgia, serif;
    font-size: 50px; font-weight: 700; line-height: 1.1; color: var(--navy);
  }
  .headline p {
    margin-top: 12px; font-size: 24px; font-style: italic; color: var(--teal);
  }

  .units {
    height: 470px; flex: none;
    display: grid; grid-template-columns: 392px 392px; gap: 31px;
    padding: 0 56px;
  }
  .unit-card {
    background: var(--white);
    border: 1px solid var(--line);
    display: flex; flex-direction: column;
  }
  .unit-photo { height: 408px; }
  .unit-curved {
    background:
      radial-gradient(ellipse 200px 70px at 50% 14%, var(--glow) 0%, rgba(255,230,166,0) 100%),
      linear-gradient(180deg, #c9ced2 0%, #e4e8eb 40%, #d3d8db 58%, #c42a24 64%, #a31a16 100%);
  }
  .unit-flat {
    background:
      radial-gradient(ellipse 200px 70px at 50% 14%, #cfe0ff 0%, rgba(207,224,255,0) 100%),
      linear-gradient(180deg, #2d4fb8 0%, #3f62cf 18%, #1e2227 26%, #7d8ea6 46%, #2a2e33 66%, #111418 100%);
  }
  .unit-caption {
    flex: 1;
    display: flex; align-items: center; justify-content: center;
    font-family: "Playfair Display", Georgia, serif;
    font-size: 22px; font-weight: 600; color: var(--navy);
    border-top: 3px solid var(--teal);
  }

  .details {
    height: 328px; flex: none;
    display: grid; grid-template-columns: 300px 1fr; gap: 31px;
    padding: 38px 56px 0;
  }
  .details h2 {
    font-family: "Playfair Display", Georgia, serif;
    font-size: 26px; font-weight: 700; color: var(--navy);
    padding-bottom: 10px; margin-bottom: 16px;
    border-bottom: 1px solid var(--line);
  }
  .spec-label { font-size: 15px; font-weight: 600; letter-spacing: 1.5px; text-transform: uppercase; color: var(--teal); }
  .spec-value { font-size: 24px; margin: 4px 0 20px; }
  .options-list { list-style: none; }
  .options-list li {
    display: flex; align-items: center; gap: 14px;
    font-size: 23px; margin-bottom: 16px;
  }
  .options-list li::before {
    content: ""; width: 10px; height: 10px; background: var(--teal); flex: none;
  }

  .contact-bar {
    flex: 1;
    background: var(--navy); color: var(--white);
    display: flex; justify-content: space-between; align-items: center;
    padding: 0 56px;
    font-size: 18px;
  }
  .contact-list { list-style: none; }
  .contact-list li { display: flex; align-items: center; gap: 16px; height: 32px; }
  .contact-list svg { width: 20px; height: 20px; fill: none; stroke: var(--white); stroke-width: 1.8; }
  .contact-address { font-style: normal; line-height: 32px; text-align: right; }
</style>
</head>
<body>
<main class="sheet">
  <header class="brand-bar">
    <span class="brand-name"><span class="brand-mark"></span>NORTHVALE DISPLAY GROUP INC.</span>
    <span class="brand-web">www.northvaledisplay.com</span>
  </header>

  <section class="headline">
    <h1>Grab N Go Refrigerated Displays</h1>
    <p>30″ 36″ &amp; 50″ Size Available</p>
  </section>

  <section class="units">
    <figure class="unit-card">
      <div class="unit-photo unit-curved" role="img" aria-label="Photo of a grab and go refrigerated display with a backlit curved header light box, grey cabinet and red base"></div>
      <figcaption class="unit-caption">Curved Header Light Box</figcaption>
    </figure>
    <figure class="unit-card">
      <div class="unit-photo unit-flat" role="img" aria-label="Photo of a black grab and go refrigerated display with a backlit flat header light box"></div>
      <figcaption class="unit-caption">Flat Header Light Box</figcaption>
    </figure>
  </section>

  <section class="details">
    <div class="specs">
      <div class="spec-label">Temperature Range</div>
      <div class="spec-value">35-46 F</div>
      <div class="spec-label">Power</div>
      <div class="spec-value">115 Volt, 9.8 Amp</div>
    </div>
    <div class="options">
      <h2>Options</h2>
      <ul class="options-list">
        <li>Custom Colors</li>
        <li>Multiple Graphics Packages Available</li>
        <li>Curved or Flat Header Light Box</li>
      </ul>
    </div>
  </section>

  <footer class="contact-bar">
    <ul class="contact-list">
      <li>
        <svg viewBox="0 0 24 24"><path d="M5 3 L9 3 L10.5 8 L8 9.5 Q10 14 14.5 16 L16 13.5 L21 15 L21 19 Q21 21 19 21 Q4 20 3 5 Q3 3 5 3 Z"/></svg>
        555-214-0187
      </li>
      <li>
        <svg viewBox="0 0 24 24"><rect x="3" y="6" width="18" height="12"/><path d="M3 6 L12 13 L21 6"/></svg>
        sales@northvaledisplay.com
      </li>
      <li>
        <svg viewBox="0 0 24 24"><circle cx="12" cy="12" r="8"/><ellipse cx="12" cy="12" rx="3.5" ry="8"/><path d="M4 12 H20"/></svg>
        www.northvaledisplay.com
      </li>
    </ul>
    <address class="contact-address">
      Northvale Display Group, Inc.<br>
      418 Meadow Park Ln<br>
      Fairbrook, IL 60917
    </address>
  </footer>
</main>
</body>
</html>
```